Halloway Consulting Cover 2 - Smart Capital

Halloway Consulting is a business consulting firm. We will publish a series of four thought leadership pieces online and via PDF. The second of the series is attached to this project. We need an eye-catching cover page with a back page that keeps with our branding. The document attached is in the final draft, and the cover and pack pages are placeholders only. You can find more about our branding and style on our website www.hallowayconsulting.com.au. The other three projects can be found here with a similar brief, and you are welcome to submit a design for all 4.

```html
<!DOCTYPE html>
<html lang="en">
<head>
<meta charset="utf-8">
<title>Halloway Consulting – Smart Capital</title>
<link href="https://fonts.googleapis.com/css2?family=Poppins:wght@400;500;600;700&display=swap" rel="stylesheet">
<style>
  :root {
    --backdrop: #a3a3a3;
    --navy: #333d48;
    --orange: #f7901e;
    --blue: #00a9ec;
    --mist: #f0f1f4;
    --white: #ffffff;
  }
  * { margin: 0; padding: 0; box-sizing: border-box; }
  html, body { width: 1200px; height: 848px; overflow: hidden; }
  body {
    background: var(--backdrop);
    font-family: "Poppins", sans-serif;
    position: relative;
  }
  .page {
    position: absolute;
    top: 27px;
    width: 560px;
    height: 793px;
    overflow: hidden;
    background: var(--navy);
    color: var(--white);
  }
  .page--cover { left: 27px; }
  .page--back { left: 613px; }
  .page-art { position: absolute; inset: 0; }

  .brand {
    position: absolute;
    display: flex;
    align-items: center;
    gap: 10px;
    font-weight: 600;
    color: var(--white);
    line-height: 1.05;
  }
  .brand-dot { border-radius: 50%; background: var(--blue); flex: none; }
  .page--cover .brand { left: 40px; top: 40px; font-size: 20px; }
  .page--cover .brand-dot { width: 44px; height: 44px; }
  .page--back .brand { left: 40px; top: 33px; font-size: 30px; gap: 14px; }
  .page--back .brand-dot { width: 70px; height: 70px; }

  .cover-title {
    position: absolute; left: 40px; top: 122px;
    font-size: 48px; font-weight: 600; color: var(--orange); line-height: 1.2;
  }
  .cover-subtitle {
    position: absolute; left: 40px; top: 186px;
    font-size: 32px; font-weight: 500; line-height: 1.3;
  }
  .cover-tagline {
    position: absolute; left: 40px; top: 293px;
    font-size: 19px; font-weight: 400;
  }
  .web-link {
    position: absolute;
    display: flex; align-items: center; gap: 7px;
    font-size: 16px; font-weight: 500; color: var(--navy);
  }
  .page--cover .web-link { left: 252px; top: 750px; }
  .page--back .web-link { left: 287px; top: 773px; }

  .contact-heading {
    position: absolute; left: 40px; top: 168px;
    font-size: 34px; font-weight: 600; color: var(--orange);
  }
  .contact-intro {
    position: absolute; left: 40px; top: 228px;
    font-size: 21px; font-weight: 500; line-height: 1.4;
  }
  .contact-intro strong { font-weight: 700; }
  .contact-person { position: absolute; left: 40px; }
  .contact-person--one { top: 334px; }
  .contact-person--two { top: 440px; }
  .person-name { font-size: 22px; font-weight: 600; color: var(--orange); line-height: 1.2; }
  .person-role { font-size: 12.5px; font-weight: 600; color: var(--blue); margin-bottom: 9px; }
  .person-detail { font-size: 13.5px; line-height: 1.35; }

  .follow {
    position: absolute; left: 40px; top: 774px;
    display: flex; align-items: center; gap: 12px;
    font-size: 12px; font-weight: 600;
  }
  .social-dot { width: 15px; height: 15px; border-radius: 50%; background: var(--white); }
</style>
</head>
<body>

<section class="page page--cover">
  <svg class="page-art" width="560" height="793" viewBox="0 0 560 793" aria-hidden="true">
    <rect x="0" y="513" width="560" height="280" fill="var(--mist)"/>
    <rect x="487" y="0" width="13" height="493" fill="var(--blue)"/>
    <rect x="487" y="413" width="13" height="380" fill="var(--orange)"/>
    <circle cx="309" cy="504" r="169" fill="var(--orange)"/>
    <circle cx="327" cy="520" r="169" fill="var(--blue)"/>
    <rect x="33" y="580" width="13" height="213" fill="var(--blue)"/>
    <rect x="73" y="633" width="13" height="160" fill="var(--orange)"/>
    <rect x="113" y="687" width="13" height="106" fill="var(--blue)"/>
    <rect x="153" y="740" width="13" height="53" fill="var(--orange)"/>
    <defs>
      <linearGradient id="towerTone" x1="0" y1="0" x2="1" y2="1">
        <stop offset="0" stop-color="#8c9bb0"/>
        <stop offset="0.5" stop-color="#7a7672"/>
        <stop offset="1" stop-color="#4a4744"/>
      </linearGradient>
    </defs>
    <circle cx="317" cy="511" r="157" fill="url(#towerTone)" role="img" aria-label="Photograph of a concrete tower rising into a blue sky"/>
  </svg>

  <div class="brand"><span class="brand-dot"></span><span>Halloway<br>Consulting</span></div>
  <h1 class="cover-title">Smart Capital:</h1>
  <p class="cover-subtitle">Partnering with funds<br>to scale your business.</p>
  <p class="cover-tagline">Bridging valuation gaps in fund raising</p>
  <div class="web-link">
    <svg width="14" height="14" viewBox="0 0 14 14" aria-hidden="true"><g fill="none" stroke="var(--navy)" stroke-width="1.4"><circle cx="7" cy="7" r="6"/><ellipse cx="7" cy="7" rx="2.6" ry="6"/><line x1="1" y1="7" x2="13" y2="7"/></g></svg>
    <span>hallowayconsulting.com.au</span>
  </div>
</section>

<section class="page page--back">
  <svg class="page-art" width="560" height="793" viewBox="0 0 560 793" aria-hidden="true">
    <polygon points="420,60 560,60 560,120 390,120" fill="var(--blue)"/>
    <polygon points="452,49 560,49 560,107 420,107" fill="var(--orange)"/>
    <polygon points="560,150 188,793 200,793 560,170" fill="var(--white)"/>
    <polygon points="560,178 206,793 560,793" fill="var(--blue)"/>
  </svg>

  <div class="brand"><span class="brand-dot"></span><span>Halloway<br>Consulting</span></div>
  <h2 class="contact-heading">Contact us</h2>
  <p class="contact-intro">Find out how <strong>Halloway Consulting</strong><br>can help build your company<br>into a market leader today.</p>

  <div class="contact-person contact-person--one">
    <p class="person-name">Daniel Halloway</p>
    <p class="person-role">Managing Director</p>
    <p class="person-detail">Mobile: +61 400 318 246<br>Email: daniel@hallowayconsulting.com.au</p>
  </div>
  <div class="contact-person contact-person--two">
    <p class="person-name">Marcus Halloway</p>
    <p class="person-role">Managing Director</p>
    <p class="person-detail">Mobile: +61 400 529 713<br>Email: marcus@hallowayconsulting.com.au</p>
  </div>

  <div class="follow"><span>Follow us</span><span class="social-dot"></span><span class="social-dot"></span></div>
  <div class="web-link">
    <svg width="14" height="14" viewBox="0 0 14 14" aria-hidden="true"><g fill="none" stroke="var(--navy)" stroke-width="1.4"><circle cx="7" cy="7" r="6"/><ellipse cx="7" cy="7" rx="2.6" ry="6"/><line x1="1" y1="7" x2="13" y2="7"/></g></svg>
    <span>hallowayconsulting.com.au</span>
  </div>
</section>

</body>
</html>
```